Wren Vehicle Polishing (Mobile detail)

I need a business card made up. I'd like it to be different in some form, either raised, embossed, debossed, something cool that stands out. (preferably embossed text somewhere in it). I will be including the Initial png file. Let me know if you need the photoshop of adobe illustrator file to work with.
Updates

Information to be included: Text: XXX-XXX-XXXX Phone: XXX-XXX-XXXX Email: wrenvehiclepolish@mailnest.example Website: www.socialpage.example/wrenvehiclepolishKTR Hours of operation: Mon - Fri 7:00AM to 8:00PM Sat - 10:00AM to 8:00PM

Target Market(s)

Mobile automotive detailing

Industry/Entity Type

Automotive

Contact Information for Business Card

Make it stand out with embossed lettering, I'd also like the background to be glossy black or matte, something that represents a shiny car, black preferred

Requirements
Must have
• A glossy background, or something.
• My logo, pick one of them that best fits your design.
Should not have
• White background,
• something that does not stand out.

```html
<!DOCTYPE html>
<html lang="en">
<head>
<meta charset="utf-8">
<title>Wren Vehicle Polishing – Business Card</title>
<link href="https://fonts.googleapis.com/css2?family=Roboto:wght@400;500&display=swap" rel="stylesheet">
<style>
  :root {
    --stage: #2c2c2c;
    --card-black: #0d0d0d;
    --card-black-light: #262626;
    --paper: #f7f7f7;
    --accent: #e8471c;
    --text-light: #f2f2f2;
    --text-dark: #1f1f1f;
    --rule: #9a9a9a;
  }
  * { margin: 0; padding: 0; box-sizing: border-box; }
  html, body { width: 1200px; height: 750px; overflow: hidden; }
  body {
    background: var(--stage);
    font-family: "Roboto", Arial, sans-serif;
    position: relative;
  }
  .card {
    position: absolute;
    left: 420px;
    width: 461px;
    height: 264px;
    overflow: hidden;
  }
  .card--front { top: 110px; background: radial-gradient(circle at 62% 40%, var(--card-black-light), var(--card-black) 60%); }
  .card--back { top: 398px; display: flex; }

  /* front */
  .front-panel { position: absolute; inset: 0; }
  .name-bar { position: absolute; left: 0; top: 30px; width: 4px; height: 32px; background: var(--text-light); }
  .person { position: absolute; left: 18px; top: 28px; }
  .person-name { color: var(--accent); font-size: 17px; font-weight: 500; line-height: 1.2; }
  .person-role { color: var(--text-light); font-size: 13px; line-height: 1.2; }
  .contacts { position: absolute; left: 18px; top: 157px; list-style: none; }
  .contacts li { display: flex; align-items: center; color: var(--text-light); font-size: 12.5px; height: 18px; }
  .contacts .icon { width: 11px; height: 11px; margin-right: 10px; flex: none; }
  .contacts .email { font-size: 11px; margin-top: 4px; }
  .brand-front {
    position: absolute; right: 18px; top: 96px;
    display: flex; align-items: center; gap: 8px;
    color: var(--text-dark); font-size: 17px; font-weight: 500;
    width: 170px; line-height: 1.15;
  }
  .brand-dot { width: 22px; height: 22px; border-radius: 50%; background: var(--accent); flex: none; }

  /* back */
  .notes { width: 227px; height: 100%; background: var(--paper); position: relative; }
  .notes span { position: absolute; left: 14px; right: 16px; height: 1px; background: var(--rule); }
  .hours-side {
    flex: 1; background: radial-gradient(circle at 50% 35%, var(--card-black-light), var(--card-black) 70%);
    display: flex; flex-direction: column; align-items: center; text-align: center;
  }
  .brand-back {
    margin-top: 60px; display: flex; align-items: center; gap: 8px;
    color: var(--text-light); font-size: 15px; font-weight: 500; width: 150px; line-height: 1.15; text-align: left;
  }
  .hours-title { margin-top: 54px; color: var(--accent); font-size: 15px; font-weight: 500; }
  .hours-line { color: var(--text-light); font-size: 12.5px; margin-top: 4px; }
</style>
</head>
<body>
  <section class="card card--front" aria-label="Business card front">
    <svg class="front-panel" viewBox="0 0 461 264" aria-hidden="true">
      <path d="M300 0 H461 V264 H215 C235 200 270 150 300 110 C285 70 290 30 300 0 Z" fill="var(--paper)"/>
    </svg>
    <div class="name-bar"></div>
    <div class="person">
      <p class="person-name">Marcus Hale</p>
      <p class="person-role">Detailer</p>
    </div>
    <ul class="contacts">
      <li><svg class="icon" viewBox="0 0 11 11"><rect x="2.5" y="0" width="6" height="11" rx="1" fill="var(--accent)"/><rect x="3.5" y="1.5" width="4" height="7" fill="var(--card-black)"/></svg>555-201-4837</li>
      <li><svg class="icon" viewBox="0 0 11 11"><path d="M0 4 Q5.5 0 11 4 L9.5 5.5 L7.5 4.5 L7.5 3.5 Q5.5 3 3.5 3.5 L3.5 4.5 L1.5 5.5 Z M2 6 H9 L10 11 H1 Z" fill="var(--accent)"/></svg>555-318-7026</li>
      <li><svg class="icon" viewBox="0 0 11 11"><rect width="11" height="11" fill="var(--accent)"/></svg>/wrenvehiclepolishKTR</li>
      <li class="email">wrenvehiclepolish@mailnest.example</li>
    </ul>
    <div class="brand-front"><span class="brand-dot"></span>Wren Vehicle Polishing</div>
  </section>

  <section class="card card--back" aria-label="Business card back">
    <div class="notes">
      <span style="top:41px"></span>
      <span style="top:79px"></span>
      <span style="top:118px"></span>
      <span style="top:158px"></span>
      <span style="top:197px"></span>
      <span style="top:236px"></span>
    </div>
    <div class="hours-side">
      <div class="brand-back"><span class="brand-dot"></span>Wren Vehicle Polishing</div>
      <p class="hours-title">HOURS OF OPERATION</p>
      <p class="hours-line">Mon - Fri 7:00AM to 8:00PM</p>
      <p class="hours-line">Sat - 10:00AM to 8:00PM</p>
    </div>
  </section>
</body>
</html>
```